TBranwell executive consulting

We need a basic clean website for executive consulting. Rosalind is the previos CIO for bluecrest airways and currently supports several technology companies with innovation and transformation.

Target Market(s)

C level technology and CIO training

Industry/Entity Type

Technology and travel industry

Coding

Coded - Design and coding required

Number of Pages Required

3 page

Font styles to use
Sans Serif

Colors
0054AA
0677BA
7BADD7
CADEEF
E8F1F8
0094D4
00A9DD
6FCCEA
C7EBF8
E9F6FB

Requirements
Must have
• Home page, about us, services social media links

```html
<!DOCTYPE html>
<html lang="en">
<head>
<meta charset="utf-8">
<title>TBranwell Executive Consulting</title>
<link href="https://fonts.googleapis.com/css2?family=Poppins:wght@400;500;600;700;800&display=swap" rel="stylesheet">
<style>
:root{
  --navy:#0a1a4a;
  --navy-deep:#06113a;
  --navy-card:#12245e;
  --blue:#0054AA;
  --blue-mid:#0677BA;
  --sky:#0094D4;
  --cyan:#00A9DD;
  --cyan-soft:#6FCCEA;
  --ice:#C7EBF8;
  --ice-pale:#E9F6FB;
  --mist:#CADEEF;
  --white:#ffffff;
  --ink:#1b2a55;
  --muted:#5b6b8c;
}
*{box-sizing:border-box;margin:0;padding:0}
html,body{width:1200px;height:4688px;overflow:hidden}
body{font-family:'Poppins',sans-serif;color:var(--ink);background:var(--white);position:relative}
.abs{position:absolute}
.btn{display:inline-flex;align-items:center;gap:8px;background:var(--cyan);color:var(--white);font-weight:600;font-size:16px;border-radius:22px;padding:10px 22px;text-decoration:none}

/* Hero */
.hero{position:absolute;left:0;top:0;width:1200px;height:900px}
.nav-logo{left:40px;top:18px;font-weight:700;font-size:34px;color:var(--white);display:flex;align-items:center;gap:10px}
.nav-logo .dot{width:14px;height:14px;border-radius:50%;background:var(--cyan)}
.nav-links{left:620px;top:38px;display:flex;gap:44px;color:var(--white);font-size:15px;font-weight:500}
.nav-phone{left:940px;top:26px;background:var(--cyan);color:var(--white);border-radius:22px;padding:10px 20px;font-size:15px;font-weight:600;display:flex;align-items:center;gap:8px}
.hero-kicker{left:104px;top:230px;color:var(--white);font-size:30px;font-weight:500}
.hero-title{left:104px;top:272px;color:var(--white);font-size:56px;font-weight:700;line-height:1.12;width:560px}
.hero-text{left:104px;top:420px;color:var(--mist);font-size:17px;line-height:1.5;width:460px}
.hero-btn{left:104px;top:508px}
.follow{left:104px;top:608px;display:flex;align-items:center;gap:12px;color:var(--white);font-size:14px;font-weight:500}
.follow .line{width:40px;height:2px;background:var(--white)}
.social{display:flex;gap:8px}
.social span{width:28px;height:28px;border-radius:50%;border:1.5px solid var(--white)}

/* Services */
.section-title{position:absolute;left:0;width:1200px;text-align:center;font-size:54px;font-weight:700;color:var(--navy)}
.services-grid{left:134px;top:1060px;width:932px;display:grid;grid-template-columns:repeat(4,212px);gap:80px 28px}
.service-card{position:relative;height:260px;background:linear-gradient(180deg,var(--navy-card),var(--navy-deep));border-radius:6px;color:var(--white);text-align:center;padding:120px 18px 0;font-weight:600;font-size:21px;line-height:1.3}
.service-card .icon{position:absolute;left:56px;top:-34px;width:100px;height:100px;border-radius:50%;background:var(--sky);border:5px solid var(--white);box-shadow:0 0 0 3px var(--cyan-soft);display:flex;align-items:center;justify-content:center}
.service-card.cta{background:var(--sky);padding-top:60px;font-size:24px}
.service-card.cta small{display:block;font-size:14px;font-weight:500;margin:8px 0 22px}
.service-card.cta a{color:var(--white);font-size:18px}

/* Stats */
.stats{left:0;top:1720px;width:1200px;height:400px;background:linear-gradient(180deg,var(--navy-deep),var(--navy))}
.stats .section-title{top:84px;color:var(--white)}
.stats-row{position:absolute;left:112px;top:192px;display:flex;gap:24px}
.stat{width:308px;height:168px;border:2px solid var(--blue-mid);border-radius:8px;background:rgba(6,119,186,.12);color:var(--white);text-align:center;padding-top:26px}
.stat b{display:block;font-size:58px;font-weight:700;line-height:1.1}
.stat span{font-size:17px}

/* About */
.about-photo{background:linear-gradient(135deg,#8a7a6a,#3a3a48);border:6px solid var(--white);box-shadow:0 8px 24px rgba(0,0,0,.2)}
.about-title{left:670px;top:2200px;font-size:54px;font-weight:700;color:var(--navy)}
.about-text{left:670px;top:2290px;width:410px;font-size:15px;line-height:1.55;color:var(--muted)}
.about-btn{left:670px;top:2460px}

/* Testimonial */
.testimonial{left:0;top:2620px;width:1200px;height:780px}
.testimonial .section-title{top:190px;color:var(--white)}
.quote-back{left:200px;top:2990px;width:880px;height:350px;background:var(--sky);border-radius:4px}
.quote-card{left:180px;top:2900px;width:840px;height:340px;background:var(--navy-card);border-radius:4px;padding:40px 70px 0;color:var(--mist);text-align:center;font-size:15px;line-height:1.55}
.quote-card .name{margin-top:18px;color:var(--white);font-weight:700;font-size:19px}
.quote-card .stars{margin-top:18px;display:inline-block;background:var(--sky);padding:4px 18px;border-radius:3px;color:var(--white);letter-spacing:4px;font-size:18px}
.quote-mark{width:64px;height:64px;border-radius:50%;background:var(--sky);border:5px solid var(--white);color:var(--white);font-size:54px;font-weight:800;text-align:center;line-height:66px}

/* Contact */
.contact-photo{left:100px;top:3480px;width:520px;height:520px;background:linear-gradient(160deg,#b3b7c2,#3c4a6b);border-radius:4px}
.contact-card{left:520px;top:3530px;width:560px;height:470px;background:var(--navy-deep);border-radius:6px;padding:30px 34px}
.contact-card h2{color:var(--white);font-size:52px;font-weight:700;margin-bottom:18px}
.form-grid{display:grid;grid-template-columns:1fr 1fr;gap:14px}
.field{background:var(--white);border-radius:6px;height:40px;padding:0 14px;display:flex;align-items:center;gap:8px;font-size:15px;color:var(--ink)}
.field.wide{grid-column:1/3;height:112px;align-items:flex-start;padding-top:10px}
.field i{width:12px;height:12px;border-radius:2px;background:var(--blue-mid)}
.submit{margin-top:20px}

/* Footer */
.footer{left:40px;top:4120px;width:1120px;height:440px;background:linear-gradient(180deg,var(--navy),var(--navy-deep));border-radius:10px;color:var(--white)}
.footer-brand{position:absolute;left:40px;top:40px;width:250px;height:360px;border:2px solid var(--blue-mid);border-radius:8px;padding:26px 22px;font-size:14px;line-height:1.55;color:var(--mist)}
.footer-brand .name{font-size:32px;font-weight:700;color:var(--white);margin-bottom:16px;display:flex;align-items:center;gap:8px}
.footer-brand .social{margin-top:22px}
.footer h4{position:absolute;font-size:20px;font-weight:600}
.footer ul{position:absolute;list-style:none;font-size:15px;line-height:1.45;color:var(--mist)}
.footer ul li{margin-bottom:12px;padding-left:16px;position:relative}
.footer ul li::before{content:"›";position:absolute;left:0;color:var(--cyan)}
.copyright{left:0;top:4576px;width:1200px;text-align:center;font-size:14px;color:var(--muted)}
</style>
</head>
<body>

<!-- Hero -->
<section class="hero">
  <svg class="abs" width="1200" height="900" viewBox="0 0 1200 900" style="left:0;top:0">
    <defs>
      <linearGradient id="heroBg" x1="0" y1="0" x2="1" y2="1">
        <stop offset="0" stop-color="#0a1a4a"/><stop offset="1" stop-color="#0d2766"/>
      </linearGradient>
      <linearGradient id="portrait" x1="0" y1="0" x2="0" y2="1">
        <stop offset="0" stop-color="#9bb0c8"/><stop offset="1" stop-color="#2a3556"/>
      </linearGradient>
    </defs>
    <path d="M0 0H1200V700C1000 840 820 880 600 760C420 660 200 740 0 860Z" fill="url(#heroBg)"/>
    <circle cx="900" cy="430" r="420" fill="#00A9DD"/>
    <circle cx="900" cy="430" r="404" fill="#ffffff"/>
    <circle cx="900" cy="430" r="396" fill="url(#portrait)" role="img" aria-label="Portrait of the consultant in front of a passenger aircraft"/>
  </svg>
  <div class="abs nav-logo"><span class="dot"></span>TBranwell</div>
  <nav class="abs nav-links"><span>HOME</span><span>ABOUT</span><span>SERVICES</span></nav>
  <div class="abs nav-phone">
    <svg width="14" height="14" viewBox="0 0 24 24"><path d="M6 2l4 4-2 3c1 3 4 6 7 7l3-2 4 4-3 4C10 22 2 14 2 5z" fill="#fff"/></svg>555-014-2290
  </div>
  <div class="abs hero-kicker">Support Technology Companies</div>
  <h1 class="abs hero-title">With Innovation &amp; Transformation</h1>
  <p class="abs hero-text">We don't just help organizations adapt to change— we help them lead it.</p>
  <a class="abs btn hero-btn">Contact Us ↗</a>
  <div class="abs follow">FOLLOW US <span class="line"></span><div class="social"><span></span><span></span><span></span><span></span></div></div>
</section>

<!-- Services -->
<h2 class="section-title" style="top:950px">Our Services</h2>
<div class="abs services-grid">
  <div class="service-card"><div class="icon"><svg width="44" height="44" viewBox="0 0 24 24" fill="none" stroke="#fff" stroke-width="1.8"><circle cx="12" cy="7" r="3"/><circle cx="5" cy="10" r="2"/><circle cx="19" cy="10" r="2"/><path d="M6 20c0-4 3-6 6-6s6 2 6 6"/></svg></div>Leadership Mentorship</div>
  <div class="service-card"><div class="icon"><svg width="44" height="44" viewBox="0 0 24 24" fill="none" stroke="#fff" stroke-width="1.8"><rect x="3" y="4" width="18" height="12" rx="1"/><path d="M8 20h8M12 16v4M7 12l3-3 3 2 4-4"/></svg></div>Technology Strategy Development</div>
  <div class="service-card"><div class="icon"><svg width="44" height="44" viewBox="0 0 24 24" fill="none" stroke="#fff" stroke-width="1.8"><rect x="6" y="2" width="12" height="20" rx="2"/><path d="M9 8h6M9 12h6M9 16h3"/></svg></div>Digital Transformation Consulting</div>
  <div class="service-card"><div class="icon"><svg width="44" height="44" viewBox="0 0 24 24" fill="none" stroke="#fff" stroke-width="1.8"><circle cx="12" cy="12" r="3"/><path d="M12 2v4M12 18v4M2 12h4M18 12h4M5 5l3 3M16 16l3 3M5 19l3-3M16 8l3-3"/></svg></div>IT-Business Partnership Development</div>
  <div class="service-card"><div class="icon"><svg width="44" height="44" viewBox="0 0 24 24" fill="none" stroke="#fff" stroke-width="1.8"><circle cx="12" cy="12" r="8"/><path d="M12 4v8l5 3"/></svg></div>Organizational Change Management</div>
  <div class="service-card"><div class="icon"><svg width="44" height="44" viewBox="0 0 24 24" fill="none" stroke="#fff" stroke-width="1.8"><rect x="4" y="3" width="16" height="18" rx="1"/><path d="M8 8l2 2 4-4M8 15h8"/></svg></div>Program and Project Oversight</div>
  <div class="service-card"><div class="icon"><svg width="44" height="44" viewBox="0 0 24 24" fill="none" stroke="#fff" stroke-width="1.8"><rect x="4" y="3" width="16" height="18" rx="1"/><path d="M8 8h8M8 12h8M8 16h5"/></svg></div>Advisory Services for CIOs and IT Executives</div>
  <div class="service-card cta">We're here ForYou<small>Let explore how TBranwell Work for you</small><a>Contact us</a></div>
</div>

<!-- Stats -->
<section class="abs stats">
  <h2 class="section-title">Our Statistics</h2>
  <div class="stats-row">
    <div class="stat"><b>20+</b><span>20 transformative years</span></div>
    <div class="stat"><b>20+</b><span>Technology Teams</span></div>
    <div class="stat"><b>40+</b><span>Career in the travel industry.</span></div>
  </div>
</section>

<!-- About -->
<div class="abs about-photo" style="left:160px;top:2160px;width:300px;height:240px" role="img" aria-label="Team meeting around a table"></div>
<div class="abs about-photo" style="left:200px;top:2290px;width:460px;height:280px;background:linear-gradient(135deg,#c9b8a6,#4a4f66)" role="img" aria-label="Colleagues working together on a laptop"></div>
<h2 class="abs about-title">About Us</h2>
<p class="abs about-text">Rosalind Branwell is a seasoned leader with a remarkable 40-year career in the travel industry, including 20 transformative years at Bluecrest Airways. As the Senior Vice President of Technology (CIO), Rosalind spearheaded some of the company's most significant technological and strategic transformations.</p>
<a class="abs btn about-btn">Read More ↗</a>

<!-- Testimonial -->
<svg class="abs" width="1200" height="780" viewBox="0 0 1200 780" style="left:0;top:2620px">
  <defs><linearGradient id="testiBg" x1="0" y1="0" x2="0" y2="1"><stop offset="0" stop-color="#0d2766"/><stop offset="1" stop-color="#06113a"/></linearGradient></defs>
  <path d="M0 120C260 20 560 0 800 60C960 100 1100 100 1200 40V780H0Z" fill="url(#testiBg)"/>
  <path d="M0 120C260 20 560 0 800 60C960 100 1100 100 1200 40" fill="none" stroke="#00A9DD" stroke-width="6"/>
</svg>
<h2 class="section-title" style="top:2804px;color:var(--white)">Testimonial</h2>
<div class="abs quote-back"></div>
<div class="abs quote-card">
  <p>Rosalind is a decisive and fair leader who exemplifies strength, wisdom, and empathy. She always possesses a clear vision for the future and is willing to make bold decisions grounded in data, expertise, and intuition while remaining open to diverse perspectives. Her leadership style fosters an inclusive environment where every voice matters, empowering her team to excel and innovate. In times of uncertainty her unwavering confidence and fairness inspire trust, guiding the organization forward with resilience and integrity.</p>
  <div class="name">Daniel Hargrove, CEO Novatrix</div>
  <div class="stars">★★★★★</div>
</div>
<div class="abs quote-mark" style="left:148px;top:2980px">“</div>
<div class="abs quote-mark" style="left:988px;top:2980px">”</div>

<!-- Contact -->
<div class="abs" style="left:0;top:3460px;width:300px;height:560px;background:radial-gradient(circle at 0 50%,rgba(0,169,221,.35),rgba(255,255,255,0) 70%)"></div>
<div class="abs contact-photo" role="img" aria-label="Two professionals reviewing work on a laptop"></div>
<div class="abs contact-card">
  <h2>Contact Us</h2>
  <div class="form-grid">
    <div class="field"><i></i>First Name</div>
    <div class="field"><i></i>Last Name</div>
    <div class="field"><i></i>Email</div>
    <div class="field"><i></i>Phone</div>
    <div class="field wide"><i></i>Message</div>
  </div>
  <a class="btn submit">Submit Now ↗</a>
</div>

<!-- Footer -->
<footer class="abs footer">
  <div class="footer-brand">
    <div class="name"><span style="width:12px;height:12px;border-radius:50%;background:var(--cyan)"></span>TBranwell</div>
    Rosalind Branwell is a seasoned leader with a remarkable 40-year career in the travel industry, including 20 transformative years at Bluecrest Airways.
    <div class="social"><span></span><span></span><span></span><span></span></div>
  </div>
  <h4 style="left:340px;top:44px">Services</h4>
  <ul style="left:340px;top:96px;width:200px">
    <li>Leadership Mentorship</li><li>Technology Strategy Development</li><li>Digital Transformation Consulting</li><li>IT-Business Partnership Development</li>
  </ul>
  <ul style="left:570px;top:96px;width:220px">
    <li>Organizational Change Management</li><li>Program and Project Oversight</li><li>Advisory Services for CIOs and IT Executives</li>
  </ul>
  <h4 style="left:820px;top:44px">Contact</h4>
  <ul style="left:820px;top:96px;width:260px">
    <li>2210 Meridian Parkway, Austin, Texas 78701</li><li>1-800-555-0147</li><li>hello@tbranwell.com</li>
  </ul>
</footer>
<div class="abs copyright">Copyright 2025 TBranwell. All Rights Reserved</div>

</body>
</html>
```